Property management company looking for modern card design

We at Blue Heron Partners provides property management services for its residential and commercial properties, with expertise in all categories of multifamily, industrial and office projects throughout California.

We need a business card design that is professional and modern designed business card. In our field, clients get hundreds of business cards, we would like our card to stand out.

Please avoid small print.

Target Market(s)

Professionals and high end clients

Industry/Entity Type

Financial Planning

Contact Information for Business Card

Company Name: Blue Heron Partners, Name, email, license #, phone number, website blueheronpartners.com

Font styles to use
Sans Serif

Requirements
Must have
• The card design needs to be adaptable because there is a possibly we will be expanding into different sectors other than real estate. The card design should be focused on financial planning and asset management.
Nice to have
• Modern and simple business card. Eye catching. Non-standard size/shaped cards would be great.
• blueheronpartners.com
Should not have
• Too many bright color or any pictures or shapes of real estate stuff.

```html
<!DOCTYPE html>
<html lang="en">
<head>
<meta charset="utf-8">
<title>Blue Heron Partners – Business Card</title>
<link rel="stylesheet" href="https://fonts.googleapis.com/css2?family=Jost:wght@400;500;600&display=swap">
<style>
  :root {
    --backdrop: #5f6675;
    --card-front: #c6b89b;
    --card-back: #2c3835;
    --brand-red: #c9161b;
    --ink: #1c1c1c;
    --ink-soft: #2b2b2b;
    --back-ink: #cdbf9f;
  }
  * { box-sizing: border-box; margin: 0; padding: 0; }
  html, body { width: 1200px; height: 1000px; overflow: hidden; }
  body {
    background: var(--backdrop);
    font-family: "Jost", sans-serif;
    position: relative;
  }
  .card {
    position: absolute;
    top: 210px;
    width: 340px;
    height: 580px;
    border-radius: 28px;
  }
  .card--front {
    left: 190px;
    background: var(--card-front);
    display: flex;
    flex-direction: column;
    align-items: center;
  }
  .card--back {
    left: 670px;
    background: var(--card-back);
  }
  .brand-name {
    margin-top: 150px;
    color: var(--brand-red);
    font-size: 30px;
    font-weight: 500;
    letter-spacing: 0.5px;
    text-transform: uppercase;
    text-align: center;
    line-height: 1.1;
  }
  .holder { margin-top: 95px; text-align: center; }
  .holder__name {
    font-size: 25px;
    font-weight: 600;
    color: var(--ink);
    letter-spacing: 0.5px;
  }
  .holder__title {
    font-size: 19px;
    font-weight: 400;
    color: var(--ink-soft);
    letter-spacing: 0.5px;
  }
  .contact { margin-top: 62px; list-style: none; }
  .contact__item {
    display: flex;
    align-items: center;
    gap: 9px;
    font-size: 15px;
    color: var(--ink-soft);
    letter-spacing: 0.4px;
    margin-bottom: 8px;
  }
  .contact__icon { width: 14px; height: 14px; fill: none; stroke: var(--ink); stroke-width: 1.6; }
  .contact__icon--solid { fill: var(--ink); stroke: none; }
  .back-brand {
    position: absolute;
    left: 50%;
    top: 50%;
    transform: translate(-50%, -50%) rotate(90deg);
    white-space: nowrap;
    color: var(--back-ink);
    font-size: 34px;
    font-weight: 500;
    letter-spacing: 1px;
    text-transform: uppercase;
  }
</style>
</head>
<body>
  <section class="card card--front">
    <div class="brand-name">Blue Heron Partners</div>
    <div class="holder">
      <p class="holder__name">YOUR NAME</p>
      <p class="holder__title">JOB TITLE</p>
    </div>
    <ul class="contact">
      <li class="contact__item">
        <svg class="contact__icon contact__icon--solid" viewBox="0 0 24 24"><path d="M6.6 10.8a15 15 0 0 0 6.6 6.6l2.2-2.2a1 1 0 0 1 1-.25 11.4 11.4 0 0 0 3.6.57 1 1 0 0 1 1 1V20a1 1 0 0 1-1 1A17 17 0 0 1 3 4a1 1 0 0 1 1-1h3.5a1 1 0 0 1 1 1c0 1.25.2 2.45.57 3.57a1 1 0 0 1-.25 1z"/></svg>
        012 - 345 - 6789
      </li>
      <li class="contact__item">
        <svg class="contact__icon" viewBox="0 0 24 24"><rect x="2" y="5" width="20" height="14"/><path d="M2 5l10 8 10-8"/></svg>
        alex@blueheronpartners.com
      </li>
      <li class="contact__item">
        <svg class="contact__icon contact__icon--solid" viewBox="0 0 24 24"><path d="M12 3l10 9h-3v9h-5v-6h-4v6H5v-9H2z"/></svg>
        www.blueheronpartners.com
      </li>
    </ul>
  </section>

  <section class="card card--back">
    <div class="back-brand">Blue Heron Partners</div>
  </section>
</body>
</html>
```